Brixley Travel letterhead design

We need a design for a simple document where we can dump our own information within it. A simple letterhead style. No address or phone details etc are required. More just our logo and free format. Hope this makes sense !

```html
<!DOCTYPE html>
<html lang="en">
<head>
<meta charset="utf-8">
<title>Brixley Travel Letterhead</title>
<link href="https://fonts.googleapis.com/css2?family=Roboto:wght@300;400;500;700&display=swap" rel="stylesheet">
<style>
  :root {
    --backdrop: #e6e6e6;
    --paper: #fcfcfc;
    --navy: #1f4275;
    --text-grey: #6e6e6e;
    --band-grey: #b9babc;
    --signature-tint: #e9edf3;
    --white: #ffffff;
  }
  html, body {
    margin: 0;
    padding: 0;
    width: 1116px;
    height: 1200px;
    overflow: hidden;
    background: var(--backdrop);
    font-family: "Roboto", Arial, sans-serif;
  }
  .letterhead {
    position: absolute;
    left: 134px;
    top: 0;
    width: 848px;
    height: 1200px;
    background: var(--paper);
    color: var(--text-grey);
  }
  .brand {
    position: absolute;
    right: 70px;
    top: 82px;
    margin: 0;
    font-size: 46px;
    font-weight: 700;
    letter-spacing: -1px;
    color: var(--navy);
    line-height: 1;
  }
  .letter-date {
    position: absolute;
    left: 70px;
    top: 268px;
    margin: 0;
    font-size: 13px;
  }
  .recipient {
    position: absolute;
    left: 70px;
    top: 325px;
    margin: 0;
    font-size: 13px;
    line-height: 19.4px;
    font-style: normal;
  }
  .recipient strong { font-weight: 500; }
  .letter-body {
    position: absolute;
    left: 70px;
    top: 440px;
    width: 708px;
    font-size: 13.6px;
    line-height: 19.3px;
  }
  .letter-body p { margin: 0 0 19.3px; text-align: justify; }
  .sign-off {
    position: absolute;
    left: 70px;
    top: 923px;
    font-size: 13px;
  }
  .sign-off .signer-name { margin: 0; font-weight: 500; }
  .signature-area {
    display: block;
    margin: 12px 0 12px -17px;
    width: 190px;
    height: 38px;
    background: var(--signature-tint);
  }
  .sign-off .signer-role { margin: 0; }
  .contact-band {
    position: absolute;
    left: 0;
    bottom: 0;
    width: 100%;
    height: 56px;
    display: flex;
  }
  .contact-band span {
    flex: 1;
    display: flex;
    align-items: center;
    justify-content: center;
    color: var(--white);
    font-size: 15px;
    font-weight: 300;
  }
  .contact-email { background: var(--navy); }
  .contact-web { background: var(--band-grey); }
</style>
</head>
<body>
  <main class="letterhead">
    <h1 class="brand">Brixley Travel</h1>

    <p class="letter-date">30/20/2016</p>

    <address class="recipient">
      <strong>Mr. XYZ Smith</strong><br>
      123, Street No. 123,<br>
      City Name<br>
      Pincode-123456
    </address>

    <section class="letter-body">
      <p>Dear Sir,</p>
      <p>Lorem Ipsum is simply dummy text of the printing and typesetting industry. Lorem Ipsum has been the industry's standard dummy text ever since the 1500s, when an unknown printer took a galley of type and scrambled it to make a type specimen book. It has survived not only five centuries, but also the leap into electronic typesetting, remaining essentially unchanged. It was popularised in the 1960s with the release of Letterfix sheets containing Lorem Ipsum passages, and more recently with desktop publishing software like Alden PageCraft including versions of Lorem Ipsum.</p>
      <p>Lorem Ipsum is simply dummy text of the printing and typesetting industry. Lorem Ipsum has been the industry's standard dummy text ever since the 1500s, when an unknown printer took a galley of type and scrambled it to make a type specimen book. It has survived not only five centuries, but also the leap into electronic typesetting, remaining essentially unchanged. It was popularised in the 1960s with the release of Letterfix sheets containing Lorem Ipsum passages, and more recently with desktop publishing software like Alden PageCraft including versions of Lorem Ipsum.</p>
      <p>Lorem Ipsum is simply dummy text of the printing and typesetting industry. Lorem Ipsum has been the industry's standard dummy text ever since the 1500s, when an unknown printer took a galley of type and scrambled it to make a type specimen book.</p>
      <p>Lorem Ipsum is simply dummy text of the printing and typesetting industry. Lorem Ipsum has been the industry's standard dummy text ever since the 1500s, when an unknown printer took a galley of type and scrambled it to make a type specimen book.</p>
    </section>

    <div class="sign-off">
      <p class="signer-name">Your Name</p>
      <span class="signature-area" role="img" aria-label="Handwritten signature"></span>
      <p class="signer-role">CEO&nbsp; |&nbsp; Owner</p>
    </div>

    <footer class="contact-band">
      <span class="contact-email">info@BrixleyTravel.com</span>
      <span class="contact-web">www.BrixleyTravel.com</span>
    </footer>
  </main>
</body>
</html>
```